Email Template for AI Website Builder Marketing Campaign

Update: All the designs submitted have too much content for an email template. I have attached a mockup example of a simplified design. Please follow this guideline to revise your design to be less "wordy" and have less content to optimize the delivery rate of the emails. I have also attached the images I used to create the mockup. Feel free to use these images for your revised designs.
Original Brief:
I need a catchy email template for my new AI Website Builder, FolioNova.ai. The template must be professional, colorful, yet not too complex. The concept of the product is this:
FolioNova uses Artificial Intelligence (AI) to instantly build stunning websites, absolutely FREE. The user simply specifies their business name and business category (industry), and their stunning new website appears before their eyes!
The template will be used in MailChimp, so please provide the code that I can simply paste into the email body.
Here is a screenshot of our new website (which is not online yet) so you can match the color scheme and style of the email template to the new website design:
https://brindlemesh.com/mock_img/7720518/2638140/58190374/q8rt2lbw4k7ehnpyd3umc0xsvo_image.jpg
Let me know if you have any questions.
Thanks!
All submitted designs are too lengthy (too much content) for an email template. I will provide a mockup showing a sample of how you can simplify your design to function better as an email template and better suit my needs. I appreciate your patience!

```html
<!DOCTYPE html>
<html lang="en">
<head>
<meta charset="UTF-8">
<title>FolioNova — Your Free AI Website</title>
<link rel="stylesheet" href="https://fonts.googleapis.com/css2?family=Open+Sans:wght@400;600;700&family=Poppins:wght@400;500;600;700&display=swap">
<style>
  :root {
    --navy: #0c2a5b;
    --navy-deep: #071d3d;
    --footer: #05203f;
    --sky: #29bdef;
    --cyan: #2bb7ea;
    --white: #ffffff;
    --ink: #1c1c1c;
    --muted: #333333;
  }
  * { box-sizing: border-box; margin: 0; padding: 0; }
  html, body { width: 1200px; height: 4014px; overflow: hidden; background: var(--white); }
  body { font-family: "Open Sans", Arial, sans-serif; color: var(--white); }

  .preheader {
    height: 100px; display: flex; align-items: center; justify-content: center;
    font-family: "Poppins", Arial, sans-serif; font-size: 28px; color: var(--ink);
    background: var(--white);
  }

  .hero {
    position: relative; height: 750px; overflow: hidden;
    background: radial-gradient(ellipse at 80% 40%, #17407c 0%, var(--navy) 45%, var(--navy-deep) 100%);
  }
  .hero-art {
    position: absolute; left: 660px; top: 100px; width: 540px; height: 600px;
    background: radial-gradient(ellipse at 60% 45%, rgba(120,170,220,.55) 0%, rgba(60,110,180,.35) 40%, rgba(12,42,91,0) 75%),
                linear-gradient(180deg, rgba(12,42,91,0) 60%, rgba(230,120,80,.35) 85%, rgba(12,42,91,0) 100%);
  }
  .brand {
    display: flex; align-items: center; gap: 18px;
    font-family: "Poppins", Arial, sans-serif; font-weight: 600; color: var(--white);
  }
  .brand-dot { border-radius: 50%; background: var(--cyan); flex: none; }
  .hero .brand { position: absolute; left: 26px; top: 152px; font-size: 70px; }
  .hero .brand-dot { width: 76px; height: 76px; }
  .hero-title {
    position: absolute; left: 34px; top: 362px;
    font-family: "Poppins", Arial, sans-serif; font-weight: 600; font-size: 51px; line-height: 72px;
  }
  .hero-title .accent { color: var(--cyan); }
  .pill {
    display: flex; align-items: center; justify-content: center; border-radius: 999px;
    font-family: "Poppins", Arial, sans-serif; font-weight: 500; text-decoration: none;
  }
  .hero .pill {
    position: absolute; left: 34px; top: 670px; width: 514px; height: 88px;
    background: var(--white); color: var(--navy); font-size: 32px;
  }

  .welcome {
    height: 2028px; background: var(--sky); text-align: center; position: relative;
  }
  .welcome-kicker { padding-top: 66px; font-size: 36px; font-weight: 400; }
  .welcome-name { font-family: "Poppins", Arial, sans-serif; font-size: 88px; font-weight: 500; line-height: 1; margin-top: 24px; }
  .welcome-lead { margin-top: 56px; font-size: 44px; font-weight: 700; line-height: 60px; }
  .devices {
    position: absolute; left: 150px; top: 520px; width: 895px; height: 790px; border-radius: 20px;
    background: linear-gradient(180deg, #1b1b1b 0%, #2d3440 8%, #dfe8ef 10%, #e8eef3 62%, #c9cfd4 66%, #9aa2aa 80%, rgba(41,189,239,0) 100%);
  }
  .welcome-body {
    position: absolute; left: 0; right: 0; top: 1442px;
    font-size: 32px; font-weight: 600; line-height: 48px; padding: 0 180px;
  }
  .welcome .pill {
    position: absolute; left: 192px; top: 1780px; width: 820px; height: 134px;
    background: var(--white); color: var(--navy); font-size: 38px;
  }

  .footer {
    height: 644px; background: var(--footer); text-align: center; position: relative;
  }
  .footer .brand { position: absolute; left: 0; right: 0; top: 136px; justify-content: center; font-size: 60px; }
  .footer .brand-dot { width: 64px; height: 64px; }
  .footer-address { position: absolute; left: 0; right: 0; top: 262px; font-size: 28px; }
  .footer .pill {
    position: absolute; left: 296px; top: 356px; width: 612px; height: 112px;
    background: var(--cyan); color: var(--white); font-size: 32px;
  }
  .footer-contact {
    position: absolute; left: 0; right: 0; top: 532px;
    font-family: "Poppins", Arial, sans-serif; font-size: 26px;
  }
  .footer-contact b { font-weight: 600; }
  .footer-contact .sep { margin: 0 18px; }

  .legal { height: 492px; background: var(--white); text-align: center; position: relative; }
  .social { position: absolute; top: 116px; left: 0; right: 0; display: flex; justify-content: center; gap: 20px; }
  .social span { width: 96px; height: 96px; border-radius: 50%; background: var(--cyan); display: block; }
  .legal-text { position: absolute; top: 310px; left: 0; right: 0; font-size: 24px; line-height: 36px; color: var(--muted); }
  .legal-text a { color: var(--muted); }
</style>
</head>
<body>
  <div class="preheader">view in web browser</div>

  <header class="hero">
    <div class="hero-art" role="img" aria-label="Glowing circuit-board brain illustration with colored tiles"></div>
    <div class="brand"><span class="brand-dot"></span>FolioNova</div>
    <h1 class="hero-title">Your <span class="accent">FREE</span> Stunning<br>Website in <span class="accent">1-Click</span> Built<br>By <span class="accent">Artificial Intelligence</span></h1>
    <a class="pill" href="#">BUILD MY FREE WEBSITE</a>
  </header>

  <section class="welcome">
    <p class="welcome-kicker">welcome to</p>
    <p class="welcome-name">FolioNova</p>
    <h2 class="welcome-lead">Harness The Power of<br>Artificial Intelligence to Instantly<br>Build Your Amazing FREE Website Today!</h2>
    <div class="devices" role="img" aria-label="Desktop, tablet and phone showing a generated business website"></div>
    <p class="welcome-body">FolioNova is the World’s first website buildr that builds professional, high-quality websites in seconds! Say gooodbye to the traditional expensive and time-consuming methods of getting your business Online!</p>
    <a class="pill" href="#">GENERATE FREE WEBSITE NOW</a>
  </section>

  <footer class="footer">
    <div class="brand"><span class="brand-dot"></span>FolioNova</div>
    <p class="footer-address">4820 Harbor Crest Road, Milford DE 19963</p>
    <a class="pill" href="#">GET YOUR FREE WEBSITE NOW</a>
    <p class="footer-contact"><b>Ph:</b> (555) 214-7730<span class="sep">|</span><b>Email:</b> hello@folionova.ai<span class="sep">|</span><b>Website:</b> www.folionova.ai</p>
  </footer>

  <section class="legal">
    <div class="social" aria-label="Social links">
      <span></span><span></span><span></span><span></span><span></span><span></span>
    </div>
    <p class="legal-text">© 2023, All Rights Reserved, FolioNova<br>Want to change how you receive these emails?<br>You can <a href="#">update your preference</a> or <a href="#">unsubscribe  from this list.</a></p>
  </section>
</body>
</html>
```